Business Card Design

New business card design

Target Market(s)

Residential & Commercial Property Managers

Industry/Entity Type

Plumbing Services

Contact Information for Business Card

Name - Owen Tredgold, title - Director, Phone Number - 0431 862 507, email - owen@rvb-plumbing.com.au, Company ABN - 73 215 904 386,

Font styles to use
Sans Serif

Colors
0054AA
0677BA
7BADD7
CADEEF
E8F1F8

```html
<!DOCTYPE html>
<html lang="en">
<head>
<meta charset="utf-8">
<title>RVB Plumbing Services – Business Card</title>
<link rel="stylesheet" href="https://fonts.googleapis.com/css2?family=Poppins:wght@300;400;500&display=swap">
<style>
  :root {
    --blue-deep: #0054AA;
    --blue-mid: #0677BA;
    --blue-soft: #7BADD7;
    --blue-pale: #CADEEF;
    --blue-mist: #E8F1F8;
    --ink: #1B2230;
    --stage: #EEF1F4;
    --white: #FFFFFF;
  }
  * { box-sizing: border-box; margin: 0; padding: 0; }
  html, body {
    width: 1200px;
    height: 720px;
    overflow: hidden;
    background: var(--stage);
    font-family: "Poppins", sans-serif;
  }
  .stage {
    width: 1200px;
    height: 720px;
    display: flex;
    align-items: center;
    justify-content: center;
    gap: 40px;
  }
  .card {
    position: relative;
    width: 540px;
    height: 340px;
    border-radius: 18px;
    overflow: hidden;
    background: var(--blue-deep);
    box-shadow: 0 14px 24px rgba(0, 40, 90, 0.22);
  }
  .card-front .swoosh {
    position: absolute;
    inset: 0;
    width: 100%;
    height: 100%;
  }
  .brand {
    position: absolute;
    display: flex;
    flex-direction: column;
    align-items: flex-end;
    line-height: 1;
  }
  .brand-name {
    font-weight: 300;
    letter-spacing: 0.04em;
  }
  .brand-tagline {
    font-weight: 300;
    letter-spacing: 0.42em;
    margin-top: 6px;
  }
  .card-front .brand {
    left: 230px;
    top: 118px;
    color: var(--ink);
  }
  .card-front .brand-name { font-size: 64px; }
  .card-front .brand-tagline { font-size: 10px; margin-right: -0.42em; }

  .card-back { color: var(--white); }
  .card-back .brand {
    right: 36px;
    top: 38px;
    color: var(--white);
  }
  .card-back .brand-name { font-size: 30px; }
  .card-back .brand-tagline { font-size: 6px; letter-spacing: 0.32em; margin-top: 3px; }

  .holder {
    position: absolute;
    left: 36px;
    top: 38px;
  }
  .holder-name {
    font-size: 33px;
    font-weight: 500;
    line-height: 1.1;
  }
  .holder-role {
    font-size: 21px;
    font-weight: 400;
    color: var(--blue-pale);
    line-height: 1.2;
  }
  .holder-abn {
    font-size: 11px;
    font-weight: 400;
    color: var(--blue-mist);
    margin-left: 8px;
    letter-spacing: 0.02em;
  }
  .contact {
    position: absolute;
    left: 36px;
    top: 218px;
    font-size: 16px;
    line-height: 1.4;
    color: var(--blue-mist);
  }
  .contact-heading {
    font-size: 15px;
    font-weight: 500;
    color: var(--white);
    margin-bottom: 10px;
    letter-spacing: 0.02em;
  }
</style>
</head>
<body>
  <main class="stage">
    <section class="card card-front" aria-label="Business card front">
      <svg class="swoosh" viewBox="0 0 540 340" aria-hidden="true">
        <ellipse cx="530" cy="160" rx="400" ry="235" fill="var(--blue-soft)" opacity="0.85"/>
        <ellipse cx="560" cy="150" rx="375" ry="215" fill="var(--blue-mist)"/>
      </svg>
      <div class="brand">
        <span class="brand-name">rvb</span>
        <span class="brand-tagline">plumbing services</span>
      </div>
    </section>

    <section class="card card-back" aria-label="Business card back">
      <div class="brand">
        <span class="brand-name">rvb</span>
        <span class="brand-tagline">plumbing services</span>
      </div>
      <div class="holder">
        <h1 class="holder-name">OWEN Tredgold</h1>
        <p class="holder-role">Director<span class="holder-abn">ABN - 73 215 904 386</span></p>
      </div>
      <div class="contact">
        <h2 class="contact-heading">CONTACT</h2>
        <p class="contact-phone">Phone Number - 0431 862 507</p>
        <p class="contact-email">email - owen@rvb-plumbing.com.au</p>
      </div>
    </section>
  </main>
</body>
</html>
```